The Quiet Harbor

I have a faux cover I will attach & want you to follow & enhance what I've created. Just an FYI, the book will be posted on brindlo & I'm working with Marrow Lane Publishing.
What you need to know:
The dimensions: 6" x 9" (15.24 x 22.86 cm)
Background color: Black
I did not capture the color of the font, so want you to get a similar gold color.
Font for title, subtitle & author name: Goudy Old Style
Font for "20th Anniversary Edition": Kunstler Script
I have thoughts of shaping the photo in an oval shape -- possibly shade out the edges?

Target Market(s)

All ages: anyone who has encountered issues with doctors, hospitals, and especially those who have struggled with cancer treatment.

Requirements
Nice to have
• Adding below another PDF, showing vintage lines that I would like to see used. Just added some text I will add to the back cover. I am waiting on one more review, which I will add. Attaching that below.

```html
<!DOCTYPE html>
<html lang="en">
<head>
<meta charset="utf-8">
<title>The Quiet Harbor — Book Cover</title>
<link href="https://fonts.googleapis.com/css2?family=Sorts+Mill+Goudy:ital@0;1&family=Pinyon+Script&display=swap" rel="stylesheet">
<style>
  :root {
    --backdrop: #cfcfcf;
    --cover-black: #050507;
    --gold-light: #eac27c;
    --gold-mid: #d9a249;
    --gold-deep: #c4861d;
    --gold-text: #dba552;
    --photo-light: #dcdcdc;
    --photo-dark: #3a3a3a;
  }
  * { margin: 0; padding: 0; box-sizing: border-box; }
  html, body {
    width: 1200px;
    height: 1200px;
    overflow: hidden;
    background: var(--backdrop);
  }
  .cover {
    position: absolute;
    left: 272px;
    top: 108px;
    width: 656px;
    height: 984px;
    background: var(--cover-black);
    font-family: "Sorts Mill Goudy", "Goudy Old Style", serif;
    color: var(--gold-text);
  }
  .title {
    position: absolute;
    top: 62px;
    left: 0;
    width: 100%;
    text-align: center;
    font-size: 58px;
    font-weight: 400;
    letter-spacing: 1px;
    line-height: 1;
    background: linear-gradient(90deg, var(--gold-light), var(--gold-mid) 55%, var(--gold-deep));
    -webkit-background-clip: text;
    background-clip: text;
    color: transparent;
  }
  .subtitle {
    position: absolute;
    top: 155px;
    left: 0;
    width: 100%;
    text-align: center;
    font-style: italic;
    font-size: 27px;
    line-height: 39px;
    letter-spacing: 0.3px;
  }
  .gold-bar {
    position: absolute;
    left: 55px;
    width: 546px;
    height: 11px;
    background: linear-gradient(90deg, var(--gold-light), var(--gold-mid) 60%, var(--gold-deep));
  }
  .gold-bar--one { top: 279px; }
  .gold-bar--two { top: 378px; }
  .gold-bar--three {
    top: 848px;
    background: linear-gradient(90deg, var(--gold-deep), var(--gold-mid) 40%, var(--gold-light));
  }
  .edition {
    position: absolute;
    top: 308px;
    left: 0;
    width: 100%;
    text-align: center;
    font-family: "Pinyon Script", cursive;
    font-size: 40px;
    line-height: 1.4;
  }
  .photo-frame {
    position: absolute;
    left: 53px;
    top: 419px;
    width: 549px;
    height: 401px;
    padding: 8px;
    background: linear-gradient(90deg, var(--gold-light), var(--gold-deep) 45%, var(--gold-light));
  }
  .author-photo {
    width: 100%;
    height: 100%;
    background: linear-gradient(180deg, var(--photo-light) 0%, #bdbdbd 45%, var(--photo-dark) 100%);
  }
  .author {
    position: absolute;
    top: 887px;
    left: 0;
    width: 100%;
    text-align: center;
    font-size: 29px;
    font-weight: 700;
    letter-spacing: 0.5px;
  }
</style>
</head>
<body>
  <main class="cover">
    <h1 class="title">THE QUIET HARBOR</h1>
    <p class="subtitle">A tale of lifelong damage from terminal cancer<br>“treatment” &amp; inhumane doctors</p>
    <div class="gold-bar gold-bar--one"></div>
    <p class="edition">20th Anniversary Edition</p>
    <div class="gold-bar gold-bar--two"></div>
    <div class="photo-frame">
      <div class="author-photo" role="img" aria-label="Black and white grainy portrait photograph of the author seated in a living room"></div>
    </div>
    <div class="gold-bar gold-bar--three"></div>
    <p class="author">Joan Reilly</p>
  </main>
</body>
</html>
```